Sandalwood Apartments —-

Letter head for my apartment building of 15 Floors
In Kampala, Uganda

SANDALWOOD APARTMENTS
47 MBERIVO CREST ROAD
NAGURU - KAMPALA
P.O. BOX 58316
KAMPALA— UGANDA

```html
<!DOCTYPE html>
<html lang="en">
<head>
<meta charset="utf-8">
<title>Sandalwood Apartments — Letterhead</title>
<link rel="stylesheet" href="https://fonts.googleapis.com/css2?family=Arimo:wght@400;700&display=swap">
<style>
  :root {
    --backdrop: #e4e4e4;
    --paper: #ffffff;
    --ink: #1f1f1f;
    --maroon: #7c2a36;
    --charcoal: #262626;
  }
  * { margin: 0; padding: 0; box-sizing: border-box; }
  html, body {
    width: 1133px;
    height: 1200px;
    overflow: hidden;
    background: var(--backdrop);
    font-family: "Arimo", Arial, sans-serif;
  }
  .letterhead {
    position: absolute;
    left: 176px;
    top: 50px;
    width: 780px;
    height: 1100px;
    background: var(--paper);
    box-shadow: 0 1px 4px rgba(0,0,0,0.12);
  }
  .brand {
    position: absolute;
    left: 70px;
    top: 88px;
    display: flex;
    align-items: center;
    gap: 12px;
  }
  .brand-mark {
    width: 16px;
    height: 16px;
    background: var(--maroon);
  }
  .brand-name {
    font-size: 21px;
    font-weight: 400;
    letter-spacing: 0.5px;
    color: var(--ink);
    line-height: 1.15;
    text-transform: uppercase;
  }
  .contact {
    position: absolute;
    right: 69px;
    top: 75px;
    text-align: right;
    color: var(--ink);
    font-size: 9.5px;
    line-height: 12px;
    text-transform: uppercase;
  }
  .contact-title { font-weight: 700; margin-bottom: 12px; }
  .contact-address { margin-bottom: 12px; }
  .contact-label { font-weight: 700; color: var(--maroon); }
  .footer-band {
    position: absolute;
    left: 0;
    bottom: 0;
    width: 780px;
    height: 18px;
    display: block;
  }
</style>
</head>
<body>
  <main class="letterhead">
    <header>
      <div class="brand">
        <span class="brand-mark"></span>
        <span class="brand-name">Sandalwood<br>Apartments</span>
      </div>
      <address class="contact" style="font-style: normal;">
        <p class="contact-title">Sandalwood Apartments</p>
        <p class="contact-address">47 Mberivo Crest Road, Naguru<br>P.O. Box 58316, Kampala— Uganda</p>
        <p><span class="contact-label">Email:</span> hello@sandalwoodapts.ug</p>
        <p><span class="contact-label">Phone:</span> 256 700 481 927</p>
      </address>
    </header>
    <svg class="footer-band" viewBox="0 0 780 18" aria-hidden="true">
      <polygon points="0,7 503,7 496,18 0,18" fill="var(--charcoal)"/>
      <polygon points="522,0 780,0 780,18 509,18" fill="var(--maroon)"/>
    </svg>
  </main>
</body>
</html>
```